We (R. T. Halvern & Associates, Inc.) are an executive Search firm based in Los Angeles that is exclusively focused in the Med Tech and Health Tech arenas.   I need a logo to communicate that we are a high end search firm, but also that we are focused in the medicine and science arenas called health tech and med tech.  Many of our clients have robotics and artificial intelligence type products, so it is very technology forward.  I tend to gravitate towards clean, sharp aesthetic as opposed to something that is really over the top.
Attached are files with my logo in two different layouts.  In addition to the letterhead and envelope, I also will need an electronic letterhead in Microsoft Word.  I tend to
I look forward to seeing the designs and just let me know if you have any questions.
Dale

```html
<!DOCTYPE html>
<html lang="en">
<head>
<meta charset="utf-8">
<title>R. T. Halvern &amp; Associates, Inc. — Stationery</title>
<link rel="stylesheet" href="https://fonts.googleapis.com/css2?family=Montserrat:wght@500;600&family=Arimo:wght@400;700&display=swap">
<style>
  :root {
    --brand-blue: #5aa6da;
    --brand-blue-light: #86c3e8;
    --brand-blue-pale: #a9d6f0;
    --ink: #1d1d1f;
    --ink-soft: #555a60;
    --paper: #f7f7f6;
    --band-black: #111214;
    --backdrop: #d7dbe0;
    --button-grey: #3a3d42;
    --mist: #dcdcdc;
  }
  * { margin: 0; padding: 0; box-sizing: border-box; }
  html, body { width: 1200px; height: 900px; overflow: hidden; }
  body {
    background: var(--backdrop);
    font-family: "Arimo", Arial, sans-serif;
    color: var(--ink);
    position: relative;
  }
  .sheet { position: absolute; overflow: hidden; box-shadow: 0 6px 18px rgba(0,0,0,.18); }

  /* Wordmark */
  .wordmark { display: flex; align-items: center; gap: 7px; }
  .wordmark__dot { border-radius: 50%; background: var(--brand-blue); flex: none; }
  .wordmark__name {
    font-family: "Montserrat", Arial, sans-serif;
    font-weight: 500;
    color: var(--ink);
    line-height: 1.15;
    letter-spacing: .04em;
    text-transform: uppercase;
  }
  .wordmark--light .wordmark__dot { background: #fff; }
  .wordmark--light .wordmark__name { color: #fff; }

  .contact { font-size: 7px; line-height: 1.45; color: var(--ink); }
  .contact__row { display: flex; align-items: center; gap: 4px; }
  .contact__icon { width: 7px; height: 7px; flex: none; }
  .divider { width: 1px; background: var(--brand-blue); align-self: stretch; }

  .mist {
    position: absolute;
    background: radial-gradient(circle at 60% 50%, rgba(200,200,200,.55), rgba(200,200,200,0) 70%);
  }

  .footer-band { position: absolute; left: 0; bottom: 0; width: 100%; }
  .footer-band__url {
    position: absolute; font-size: 7px; color: #d8d8d8; letter-spacing: .08em;
  }

  /* Letterhead */
  .letterhead { left: 40px; top: 40px; width: 440px; height: 622px; background: var(--paper); }
  .letterhead__header { position: absolute; left: 34px; top: 34px; right: 30px; display: flex; align-items: flex-start; gap: 12px; }
  .letterhead__header .wordmark__name { font-size: 11px; }
  .letterhead__header .wordmark__dot { width: 14px; height: 14px; }
  .letterhead__details { margin-left: auto; display: flex; gap: 8px; }
  .letterhead__body { position: absolute; left: 34px; top: 104px; width: 370px; font-size: 7.5px; line-height: 1.55; color: var(--ink-soft); }
  .letterhead__date { margin-bottom: 10px; }
  .letterhead__recipient { margin-bottom: 10px; }
  .letterhead__recipient strong { color: var(--ink); }
  .letterhead__body p { margin-bottom: 8px; }
  .letterhead__closing { margin-top: 14px; }
  .signature { width: 110px; height: 22px; margin: 4px 0 3px; background: linear-gradient(90deg, #e6e6e6, #f1f1f1); border-radius: 3px; }
  .letterhead__signer { color: var(--ink); font-weight: 700; }

  /* Letterhead reverse */
  .letterhead-reverse { left: 510px; top: 250px; width: 260px; height: 368px; background: var(--brand-blue); }

  /* DL envelope */
  .envelope-dl { left: 510px; top: 40px; width: 360px; height: 180px; background: var(--paper); }
  .envelope-dl__header { position: absolute; left: 20px; top: 18px; }
  .envelope-dl__header .wordmark__name { font-size: 9px; }
  .envelope-dl__header .wordmark__dot { width: 12px; height: 12px; }
  .envelope-dl__details { position: absolute; left: 20px; top: 54px; display: flex; gap: 8px; }

  /* Document envelope */
  .document-envelope { left: 800px; top: 250px; width: 360px; height: 480px; background: var(--brand-blue); }
  .document-envelope__mark { position: absolute; left: 0; right: 0; top: 240px; display: flex; justify-content: center; }
  .document-envelope__mark .wordmark__name { font-size: 14px; }
  .document-envelope__mark .wordmark__dot { width: 18px; height: 18px; }

  /* Business cards */
  .card { width: 240px; height: 140px; top: 720px; }
  .card--front { left: 40px; background: var(--paper); }
  .card--back { left: 300px; background: var(--brand-blue); }
  .card__details { position: absolute; left: 14px; top: 14px; }
  .card__mark { position: absolute; right: 14px; top: 56px; text-align: right; }
  .card__mark .wordmark__name { font-size: 8px; }
  .card__mark .wordmark__dot { width: 10px; height: 10px; }
  .card__person { position: absolute; right: 14px; top: 86px; text-align: right; font-size: 7px; color: var(--ink); }
  .card__person-name { color: var(--brand-blue); font-weight: 700; font-size: 8px; }
  .card--back .wordmark { position: absolute; left: 0; right: 0; top: 52px; justify-content: center; }
  .card--back .wordmark__name { font-size: 10px; }
  .card--back .wordmark__dot { width: 12px; height: 12px; }
  .card__url { position: absolute; left: 0; right: 0; top: 92px; text-align: center; font-size: 6.5px; letter-spacing: .14em; color: #e8f4fb; }
</style>
</head>
<body>

<svg width="0" height="0" style="position:absolute">
  <defs>
    <symbol id="icon-phone" viewBox="0 0 10 10"><path d="M2 1h2l1 2.5-1.3.8a5 5 0 0 0 2 2L6.5 5 9 6v2a1 1 0 0 1-1 1A7 7 0 0 1 1 2a1 1 0 0 1 1-1z" fill="#5aa6da"/></symbol>
    <symbol id="icon-mail" viewBox="0 0 10 10"><rect x="1" y="2.5" width="8" height="5.5" rx=".6" fill="#5aa6da"/><path d="M1.3 3l3.7 2.7L8.7 3" stroke="#fff" stroke-width=".8" fill="none"/></symbol>
  </defs>
</svg>

<!-- Letterhead -->
<section class="sheet letterhead">
  <header class="letterhead__header">
    <div class="wordmark">
      <span class="wordmark__dot"></span>
      <span class="wordmark__name">R. T. Halvern<br>&amp; Associates, Inc.</span>
    </div>
    <div class="letterhead__details">
      <span class="divider"></span>
      <div class="contact">
        <div class="contact__row"><svg class="contact__icon"><use href="#icon-phone"/></svg>+1.424.555.0182</div>
        <div class="contact__row"><svg class="contact__icon"><use href="#icon-phone"/></svg>+1.424.555.0193</div>
        <div class="contact__row"><svg class="contact__icon"><use href="#icon-mail"/></svg>info@rthalvern.com</div>
      </div>
      <span class="divider"></span>
      <div class="contact">2250 Meridian Ave<br>Suite #410<br>Torrance CA 90505</div>
    </div>
  </header>

  <div class="letterhead__body">
    <div class="letterhead__date">01 January 2050</div>
    <div class="letterhead__recipient"><strong>Company (Pvt) Ltd.</strong><br>PO Box 3255 Mainville St<br>Sample City Country 3355</div>
    <p>Dear Alan Whitcombe,</p>
    <p>Dolor sit amet, consectetuer adipiscing elit, sed diam nonummy nibh euismod tincidunt ut laoreet dolore magna aliquam erat volutpat. Ut wisi enim ad minim veniam, quis nostrud exerci tation ullamcorper suscipit lobortis nisl ut aliquip ex ea commodo consequat.</p>
    <p>Consectetuer adipiscing elit, sed diam nonummy nibh euismod tincidunt ut laoreet dolore magna aliquam erat volutpat. Ut wisi enim ad minim veniam, quis nostrud exerci tation ullamcorper suscipit lobortis nisl ut aliquip ex ea commodo consequat.</p>
    <p>Sed diam nonummy nibh euismod tincidunt ut laoreet dolore magna aliquam erat volutpat. Ut wisi enim ad minim veniam, quis nostrud exerci tation ullamcorper suscipit lobortis nisl ut aliquip ex ea commodo consequat.</p>
    <div class="letterhead__closing">Sincerely Yours</div>
    <div class="signature" role="img" aria-label="Handwritten signature of Dale Halvern"></div>
    <div class="letterhead__signer">Dale Halvern</div>
  </div>

  <div class="mist" role="img" aria-label="Soft grey circle motif" style="left:200px;top:420px;width:240px;height:150px;"></div>

  <svg class="footer-band" width="440" height="70" viewBox="0 0 440 70" aria-hidden="true">
    <path d="M0 14 Q220 64 440 36 L440 70 L0 70 Z" fill="#5aa6da"/>
    <path d="M0 18 Q220 68 440 40 L440 70 L0 70 Z" fill="#111214"/>
  </svg>
  <span class="footer-band__url" style="left:40px;bottom:10px;">www.rthalvern.com</span>
</section>

<!-- Envelope (DL) -->
<section class="sheet envelope-dl">
  <div class="envelope-dl__header wordmark">
    <span class="wordmark__dot"></span>
    <span class="wordmark__name">R. T. Halvern<br>&amp; Associates, Inc.</span>
  </div>
  <div class="envelope-dl__details">
    <div class="contact">
      <div class="contact__row"><svg class="contact__icon"><use href="#icon-phone"/></svg>+1.424.555.0182</div>
      <div class="contact__row"><svg class="contact__icon"><use href="#icon-phone"/></svg>+1.424.555.0193</div>
      <div class="contact__row"><svg class="contact__icon"><use href="#icon-mail"/></svg>info@rthalvern.com</div>
    </div>
    <span class="divider"></span>
    <div class="contact">2250 Meridian Ave<br>Suite #410<br>Torrance CA 90505</div>
  </div>
  <div class="mist" role="img" aria-label="Soft grey circle motif" style="left:210px;top:40px;width:160px;height:110px;"></div>
  <svg class="footer-band" width="360" height="44" viewBox="0 0 360 44" aria-hidden="true">
    <path d="M0 6 Q180 40 360 26 L360 44 L0 44 Z" fill="#5aa6da"/>
    <path d="M0 9 Q180 43 360 29 L360 44 L0 44 Z" fill="#111214"/>
  </svg>
  <span class="footer-band__url" style="left:150px;bottom:5px;font-size:6px;">www.rthalvern.com</span>
</section>

<!-- Letterhead reverse -->
<section class="sheet letterhead-reverse" aria-label="Letterhead reverse side"></section>

<!-- Document envelope -->
<section class="sheet document-envelope">
  <svg width="360" height="480" viewBox="0 0 360 480" style="position:absolute;left:0;top:0" aria-hidden="true">
    <path d="M0 480 L40 430 L320 430 L360 480 Z" fill="#86c3e8"/>
    <path d="M360 90 L318 120 L318 430 L360 480 Z" fill="#a9d6f0"/>
    <path d="M0 0 L360 0 L360 90 L330 120 L30 120 L0 90 Z" fill="#86c3e8"/>
    <line x1="180" y1="104" x2="180" y2="150" stroke="#e8eef2" stroke-width="1.2"/>
    <line x1="176" y1="104" x2="184" y2="150" stroke="#e8eef2" stroke-width="1"/>
    <circle cx="180" cy="104" r="11" fill="#3a3d42"/>
    <circle cx="180" cy="104" r="2.5" fill="#8a8d92"/>
    <circle cx="180" cy="150" r="11" fill="#3a3d42"/>
    <circle cx="180" cy="150" r="2.5" fill="#8a8d92"/>
  </svg>
  <div class="document-envelope__mark">
    <div class="wordmark wordmark--light">
      <span class="wordmark__dot"></span>
      <span class="wordmark__name">R. T. Halvern<br>&amp; Associates, Inc.</span>
    </div>
  </div>
</section>

<!-- Business card, front -->
<section class="sheet card card--front">
  <div class="card__details contact" style="font-size:6px;">
    2250 Meridian Ave<br>Suite #410<br>Torrance CA 90505
    <div class="contact__row" style="margin-top:4px;"><svg class="contact__icon"><use href="#icon-phone"/></svg>+1.424.555.0182</div>
    <div class="contact__row"><svg class="contact__icon"><use href="#icon-phone"/></svg>+1.424.555.0193</div>
    <div class="contact__row"><svg class="contact__icon"><use href="#icon-mail"/></svg>info@rthalvern.com</div>
  </div>
  <div class="card__mark wordmark">
    <span class="wordmark__dot"></span>
    <span class="wordmark__name">R. T. Halvern<br>&amp; Associates, Inc.</span>
  </div>
  <div class="card__person">
    <div class="card__person-name">Dale Halvern</div>
    Executive Recruiter
  </div>
  <svg class="footer-band" width="240" height="34" viewBox="0 0 240 34" aria-hidden="true">
    <path d="M0 4 Q120 30 240 22 L240 34 L0 34 Z" fill="#5aa6da"/>
    <path d="M0 7 Q120 33 240 25 L240 34 L0 34 Z" fill="#111214"/>
  </svg>
  <span class="footer-band__url" style="left:96px;bottom:2px;font-size:5.5px;">www.rthalvern.com</span>
</section>

<!-- Business card, back -->
<section class="sheet card card--back">
  <div class="mist" role="img" aria-label="Soft pale circle motif" style="left:120px;top:0;width:140px;height:80px;background:radial-gradient(circle at 50% 50%, rgba(255,255,255,.22), rgba(255,255,255,0) 70%);"></div>
  <div class="wordmark wordmark--light">
    <span class="wordmark__dot"></span>
    <span class="wordmark__name">R. T. Halvern<br>&amp; Associates, Inc.</span>
  </div>
  <div class="card__url">www.rthalvern.com</div>
</section>

</body>
</html>
```